Independent Statistical Consultant Business Card

I will be going out as an independent statistical consultant and need a business card. I specialize in data analysis and statistics for health care and public health

I am an Licensed Numeric Examiner from the Coastal Metrics Society. Would like to incorporate that logo into the design

The design should be modern with classic colors, convey accuracy, analytic creativity and responsiveness to client needs.

The name of the firm will be simply Tim Halvarsen Numeric Insight Services

To all designers, I want to clarify that the DCred logo and the phrase Licensed Numeric Examiner are not the name of the company nor the focus of the card. They are equivalent to being a Veltrano Qualified Engineer (VQE) but in the area of statistics The name of the firm will be: Tim Halvarsen, Numeric Insight Services. I look forward to your submissions. Thanks. Tim

```html
<!DOCTYPE html>
<html lang="en">
<head>
<meta charset="utf-8">
<title>Tim Halvarsen – Business Card</title>
<link rel="stylesheet" href="https://fonts.googleapis.com/css2?family=Ubuntu:wght@300;400&display=swap">
<style>
  :root {
    --page: #141414;
    --card: #262626;
    --teal: #3fa3b8;
    --teal-bright: #5ec6d3;
    --teal-pale: #c9e9ef;
    --teal-deep: #3d9fb3;
    --text-light: #e6e6e6;
    --rule: #7a7a7a;
    --badge: #ffffff;
  }
  html, body {
    margin: 0;
    width: 1200px;
    height: 800px;
    overflow: hidden;
    background: var(--page);
    font-family: "Ubuntu", sans-serif;
  }
  .card {
    position: absolute;
    left: 120px;
    top: 126px;
    width: 960px;
    height: 548px;
    background: var(--card);
    overflow: hidden;
  }
  .brand-mark {
    position: absolute;
    left: 76px;
    top: 72px;
    width: 140px;
    height: 140px;
    border-radius: 50%;
    background: var(--teal);
  }
  .brand-name {
    position: absolute;
    left: 262px;
    top: 98px;
    margin: 0;
    color: var(--teal);
    font-weight: 400;
    line-height: 1;
  }
  .brand-name .firm-owner { display: block; font-size: 56px; }
  .brand-name .firm-service { display: block; font-size: 23px; margin-top: 2px; padding-left: 4px; }
  .person {
    position: absolute;
    left: 72px;
    top: 284px;
    margin: 0;
    color: var(--teal);
    font-weight: 400;
    font-size: 40px;
    line-height: 1;
  }
  .person .role {
    color: var(--text-light);
    font-size: 23px;
    margin-left: 8px;
  }
  .divider {
    position: absolute;
    left: 72px;
    top: 357px;
    width: 816px;
    height: 2px;
    background: var(--rule);
  }
  .contacts {
    position: absolute;
    left: 72px;
    top: 380px;
    margin: 0;
    padding: 0;
    list-style: none;
    color: var(--text-light);
    font-size: 26px;
    font-weight: 400;
  }
  .contacts li { display: flex; align-items: center; height: 42px; }
  .contacts .item { display: inline-flex; align-items: center; margin-right: 28px; }
  .contacts svg { width: 24px; height: 24px; margin-right: 10px; fill: var(--teal-bright); }
  .credential-badge {
    position: absolute;
    left: 722px;
    top: 378px;
    width: 166px;
    height: 72px;
    background: var(--badge);
  }
  .accent-bars { position: absolute; left: 0; bottom: 2px; width: 960px; height: 30px; }
  .accent-bars span { position: absolute; top: 0; height: 30px; }
  .bar-one { left: 0; width: 270px; background: var(--teal-bright); }
  .bar-two { left: 284px; width: 312px; background: var(--teal-pale); }
  .bar-three { left: 610px; width: 350px; background: var(--teal-deep); }
</style>
</head>
<body>
  <div class="card">
    <div class="brand-mark" aria-hidden="true"></div>
    <h1 class="brand-name">
      <span class="firm-owner">Tim Halvarsen</span>
      <span class="firm-service">Numeric Insight Services</span>
    </h1>

    <h2 class="person">TIM HALVARSEN<span class="role">Statistic Consultant</span></h2>
    <div class="divider"></div>

    <ul class="contacts">
      <li>
        <span class="item">
          <svg viewBox="0 0 24 24" aria-label="Phone"><rect x="3" y="2" width="7" height="20" rx="1"/><rect x="11" y="5" width="10" height="15" rx="1"/></svg>
          +61 198765430
        </span>
        <span class="item">
          <svg viewBox="0 0 24 24" aria-label="Fax"><rect x="7" y="2" width="10" height="6"/><rect x="3" y="9" width="18" height="9" rx="1"/><rect x="7" y="15" width="10" height="7"/></svg>
          +61 198765430
        </span>
      </li>
      <li>
        <span class="item">
          <svg viewBox="0 0 24 24" aria-label="Email"><path d="M2 5h20v14H2z M2 5l10 8 10-8" /></svg>
          timhalvarsen@mailnest.com
        </span>
      </li>
    </ul>

    <div class="credential-badge" role="img" aria-label="Licensed Numeric Examiner credential badge"></div>

    <div class="accent-bars" aria-hidden="true">
      <span class="bar-one"></span>
      <span class="bar-two"></span>
      <span class="bar-three"></span>
    </div>
  </div>
</body>
</html>
```